Card design for Heating and Cooling company

this is for a heating and cooling company we recently updated our logo and need to update our cards. We attached our logo so you can incorporate it into the card. We specialize in residential and commercial furnace and air condition repairs. Have been in business since 2014.

Phone number 555.284.9137

We need the following phrases
:Repairs, Installations, and maintenance
:Quality work at reasonable prices
:residential/commercial
:Licensed &Insured
:Email Pinegrovehvac47@mailbox-example.com
Name: Teodor K (Ted)
Also on back side I would like my logo with wording :Thank you for your business and refferal

Industry/Entity Type

Hvac

Contact Information for Business Card

:residential/commercial
:Licensed & Insured
Name: Teodor K (Ted)
Number:555.284.9136

Requirements
Must have
• Blue and red colors
Nice to have
• Maybe a pic of a furnace or air conditioner

```html
<!DOCTYPE html>
<html lang="en">
<head>
<meta charset="utf-8">
<title>Pinegrove Heating &amp; Cooling – Thank You Card</title>
<link rel="stylesheet" href="https://fonts.googleapis.com/css2?family=Bodoni+Moda:ital,opsz,wght@0,6..96,900;1,6..96,900&display=swap">
<style>
  :root {
    --page: #ffffff;
    --card-top: #ffffff;
    --card-bottom: #e4e4e4;
    --brand-grey: #838383;
    --ink: #111111;
    --warm-red: #ee2a2a;
    --warm-pink: #f0a0a0;
    --cool-blue: #1e9fdc;
    --cool-deep: #0a56a4;
    --cool-light: #a8dcf0;
  }
  html, body {
    margin: 0;
    padding: 0;
    width: 1200px;
    height: 1000px;
    overflow: hidden;
    background: var(--page);
  }
  .canvas {
    position: relative;
    width: 1200px;
    height: 1000px;
  }
  .card-back {
    position: absolute;
    left: 0;
    top: 157px;
    width: 1200px;
    height: 686px;
    background: linear-gradient(to bottom, var(--card-top) 25%, var(--card-bottom) 100%);
    overflow: hidden;
  }
  .corner-art {
    position: absolute;
    left: 0;
    top: 0;
    width: 1200px;
    height: 686px;
  }
  .brand {
    position: absolute;
    left: 0;
    top: 300px;
    width: 1200px;
    text-align: center;
    font-family: "Bodoni Moda", "Times New Roman", serif;
    font-weight: 900;
    font-style: normal;
    color: var(--brand-grey);
  }
  .brand-name {
    display: block;
    font-size: 76px;
    line-height: 1;
    letter-spacing: 1px;
  }
  .brand-tagline {
    display: block;
    margin-top: 10px;
    font-size: 20px;
    letter-spacing: 16px;
    padding-left: 16px;
  }
  .brand-mark {
    position: absolute;
    left: 560px;
    top: 190px;
    width: 80px;
    height: 80px;
    border-radius: 50%;
    background: var(--cool-light);
  }
  .thanks {
    position: absolute;
    left: 12px;
    bottom: 22px;
    margin: 0;
    font-family: "Bodoni Moda", "Times New Roman", serif;
    font-weight: 900;
    font-style: italic;
    font-size: 29px;
    color: var(--ink);
  }
</style>
</head>
<body>
<div class="canvas">
  <section class="card-back">
    <svg class="corner-art" viewBox="0 0 1200 686" xmlns="http://www.w3.org/2000/svg">
      <defs>
        <linearGradient id="top-band-fill" x1="0" y1="0" x2="1" y2="0">
          <stop offset="0" stop-color="var(--warm-red)"/>
          <stop offset="0.4" stop-color="var(--warm-pink)"/>
          <stop offset="0.7" stop-color="var(--cool-blue)"/>
          <stop offset="1" stop-color="var(--cool-light)" stop-opacity="0.5"/>
        </linearGradient>
        <linearGradient id="bottom-band-fill" x1="0" y1="0" x2="1" y2="0">
          <stop offset="0" stop-color="var(--cool-light)" stop-opacity="0.5"/>
          <stop offset="0.35" stop-color="var(--cool-blue)"/>
          <stop offset="0.6" stop-color="var(--cool-deep)"/>
          <stop offset="0.8" stop-color="var(--warm-pink)"/>
          <stop offset="1" stop-color="var(--warm-red)"/>
        </linearGradient>
      </defs>
      <polygon class="corner-band corner-band--top" role="img"
               aria-label="Decorative band of red and blue squares"
               points="0,0 600,0 0,230" fill="url(#top-band-fill)" opacity="0.85"/>
      <polygon class="corner-band corner-band--bottom" role="img"
               aria-label="Decorative band of blue and red squares"
               points="620,686 1200,686 1200,480" fill="url(#bottom-band-fill)" opacity="0.85"/>
    </svg>

    <div class="brand-mark"></div>
    <div class="brand">
      <span class="brand-name">PINEGROVE</span>
      <span class="brand-tagline">HEATING &amp; COOLING</span>
    </div>

    <p class="thanks">Thank you for your business and refferal</p>
  </section>
</div>
</body>
</html>
```